The most modern business card ever !!!

Our company call “Vantilo”. Vantilo is a technology company specialized in cruises solutions. Out main product is a platform to reserve cruises. This is a revolutionary platform that make easier to travel agencies and final users to reserve cruises across dozen companies like tarvik, welbi, dpv, hbt, etc..We are a “start up”, with a young team of developers and we want to transmit it.. For it, we want something different, a modern business card that represent cruises and technology.. When someone receive this card, this person should say: wowww this is different… this is modern… this is a cruise related company..
Contact Information for Business Card
Requirements
Must have
- diferent, modern
Should not have
- traditions business card

```html
<!DOCTYPE html>
<html lang="en">
<head>
<meta charset="utf-8">
<title>Vantilo — Business Card</title>
<link href="https://fonts.googleapis.com/css2?family=Exo+2:wght@400;500;600&display=swap" rel="stylesheet">
<style>
  :root {
    --bg: #d9dbde;
    --card-white: #ffffff;
    --ink: #111111;
    --accent: #22a8de;
    --sky-top: #6f86c8;
    --sky-mid: #9fb2dc;
    --sea: #4d6e9c;
    --muted: #2a2a2a;
  }
  * { box-sizing: border-box; margin: 0; padding: 0; }
  html, body {
    width: 1200px; height: 1200px; overflow: hidden;
    background: var(--bg);
    font-family: "Exo 2", sans-serif;
  }
  .stage {
    position: relative; width: 1200px; height: 1200px;
  }
  .card {
    position: absolute; left: 170px;
    width: 860px; height: 491px;
    overflow: hidden;
    box-shadow: 0 10px 28px rgba(0,0,0,0.22);
  }
  /* Front side */
  .card--front { top: 88px; }
  .card__photo {
    position: absolute; inset: 0;
    background: linear-gradient(180deg, var(--sky-top) 0%, var(--sky-mid) 55%, var(--sea) 70%, #3f5f8e 100%);
  }
  .card--front .brand {
    position: absolute; left: 70px; top: 60px;
    font-size: 76px; font-weight: 600; color: var(--ink);
    letter-spacing: 2px; line-height: 1;
  }
  /* Back side */
  .card--back { top: 618px; background: var(--card-white); }
  .card--back .brand {
    position: absolute; left: 72px; top: 70px;
    font-size: 118px; font-weight: 600; color: var(--ink);
    letter-spacing: 3px; line-height: 1;
  }
  .person {
    position: absolute; right: 70px; top: 112px; text-align: right;
  }
  .person__name { font-size: 36px; font-weight: 500; color: var(--ink); letter-spacing: 1px; }
  .person__role { font-size: 21px; font-weight: 500; color: var(--accent); letter-spacing: 2px; margin-top: 2px; }
  .contact {
    position: absolute; left: 78px; top: 262px;
    font-size: 19px; color: var(--muted); letter-spacing: 0.8px; line-height: 1.55;
    list-style: none;
  }
  .contact li { display: flex; align-items: center; gap: 10px; }
  .contact .address { padding-left: 0; }
  .contact svg { width: 18px; height: 18px; fill: var(--accent); flex: none; }
  .bands { position: absolute; inset: 0; width: 100%; height: 100%; }
</style>
</head>
<body>
<main class="stage">

  <section class="card card--front">
    <div class="card__photo" role="img" aria-label="Photograph of a large white cruise ship sailing on blue sea under a clear sky"></div>
    <div class="brand">Vantilo</div>
  </section>

  <section class="card card--back">
    <svg class="bands" viewBox="0 0 860 491" preserveAspectRatio="none" aria-hidden="true">
      <polygon points="500,362 860,318 860,491 590,491" fill="var(--accent)"/>
      <polygon points="420,392 860,348 860,491 380,491" fill="var(--card-white)"/>
      <polygon points="430,400 860,356 860,491 300,491" fill="var(--ink)"/>
    </svg>

    <div class="brand">Vantilo</div>

    <div class="person">
      <div class="person__name">Milo Harten</div>
      <div class="person__role">Director</div>
    </div>

    <ul class="contact">
      <li class="address">Dummy city</li>
      <li class="address">Dummy Country Land</li>
      <li>
        <svg viewBox="0 0 24 24"><path d="M3 9c0-3 4-5 9-5s9 2 9 5l-4 1-1-3H8L7 10 3 9zm3 3h12l2 7H4l2-7zm6 1.5a2.5 2.5 0 1 0 0 5 2.5 2.5 0 0 0 0-5z"/></svg>
        1-234-567890
      </li>
      <li>
        <svg viewBox="0 0 24 24"><path d="M7 2h10a1 1 0 0 1 1 1v18a1 1 0 0 1-1 1H7a1 1 0 0 1-1-1V3a1 1 0 0 1 1-1zm1 3v12h8V5H8zm4 13.5a1 1 0 1 0 0 2 1 1 0 0 0 0-2z"/></svg>
        1-234-567890
      </li>
      <li>
        <svg viewBox="0 0 24 24"><path d="M12 2a10 10 0 1 0 0 20 10 10 0 0 0 0-20zm6.9 9h-3a15 15 0 0 0-1.3-6 8 8 0 0 1 4.3 6zM12 4c.9 1.2 1.8 3.6 1.9 7h-3.8c.1-3.4 1-5.8 1.9-7zM9.4 5a15 15 0 0 0-1.3 6h-3a8 8 0 0 1 4.3-6zM5.1 13h3a15 15 0 0 0 1.3 6 8 8 0 0 1-4.3-6zM12 20c-.9-1.2-1.8-3.6-1.9-7h3.8c-.1 3.4-1 5.8-1.9 7zm2.6-1a15 15 0 0 0 1.3-6h3a8 8 0 0 1-4.3 6z"/></svg>
        www.vantilo.com
      </li>
      <li>
        <svg viewBox="0 0 24 24"><path d="M2 5h20v14H2V5zm2 2v.5l8 5.5 8-5.5V7H4zm0 3v7h16v-7l-8 5.5L4 10z"/></svg>
        milo@vantilo.com
      </li>
    </ul>
  </section>

</main>
</body>
</html>
```